Banner for home page on event planning site

We are revamping the home page www.coralbellecelebrations.com and would like to add a banner to the center of it to guide potential clients to one of 3 areas of the site:

Weddings, Corporate Events, Parties and More

I'm uploading an attachment that shows where the banner will be placed. It needs to have those 3 distinct sections, and match the existing colors/branding of the site. The fonts used for the logo are Lucida Bright and Callie Hand. Both are available for free.

Please use lorem ipsum under each section, I'll fill that in later. It should just be highly designed, beautiful, and easy to understand that clicking these will take you to the different areas of the site.
Updates

Hi designers,
Here are some problems we are having with the designs that have been submitted.
1) 3 stock images as squares... when you do this and then put it into the existing website, it gets lost among the other boxes. We need this to be where the eye goes immediately when you land on the site.
2) Not enough of a frame or white space... we think you need some white space to make this stand out as different from the surrounding area.
3) No clearly defined areas. It needs to be easy for people to figure out... Weddings, click here. Parties, click here. Corporate events, click here.

Industry/Entity Type

Event Planning

Requirements
Should not have
• Nothing with orchids, her competitor uses them and they are common in the event planning industry. We want to stay away from them.

Files

```html
<!DOCTYPE html>
<html lang="en">
<head>
<meta charset="utf-8">
<title>Coral Belle Events – Home</title>
<link rel="stylesheet" href="https://fonts.googleapis.com/css2?family=Open+Sans:wght@400;600&family=Lora:wght@400&display=swap">
<style>
  :root {
    --brand: #a8367c;
    --brand-soft: #b4558f;
    --ink: #2f2f2f;
    --muted: #7a7a7a;
    --panel: #efede7;
    --frame: #111111;
    --page: #ffffff;
    --divider: #cfcbc3;
    --team-bg: #f3f0f1;
  }
  * { box-sizing: border-box; margin: 0; padding: 0; }
  html, body { width: 1200px; height: 607px; overflow: hidden; background: var(--page); }
  body { position: relative; font-family: "Open Sans", sans-serif; color: var(--ink); }

  .sidebar { position: absolute; left: 0; top: 0; width: 176px; height: 607px; background: var(--page); border-right: 3px solid var(--brand); }
  .brand { position: absolute; left: 14px; top: 22px; width: 160px; }
  .brand-name { font-family: "Lora", serif; font-size: 18px; color: var(--brand); white-space: nowrap; }
  .brand-tagline { font-size: 6.5px; letter-spacing: .3px; color: var(--muted); margin-top: 3px; white-space: nowrap; }

  .main-nav { position: absolute; left: 11px; top: 83px; width: 165px; list-style: none; }
  .main-nav li { height: 24.7px; line-height: 24.7px; padding: 0 22px 0 8px; font-size: 11.5px; text-transform: uppercase; color: var(--brand-soft); position: relative; white-space: nowrap; }
  .main-nav li.is-active { background: var(--brand); color: #fff; }
  .main-nav li.has-sub::after { content: "›"; position: absolute; right: 9px; top: 0; font-size: 12px; }

  .social-row { position: absolute; left: 28px; top: 516px; display: flex; gap: 5px; }
  .social-row span { width: 16px; height: 16px; border-radius: 50%; background: #a9a9a9; }
  .search-box { position: absolute; left: 11px; top: 544px; width: 155px; height: 19px; border: 1px solid #ccc; border-radius: 10px; font-size: 9px; color: var(--muted); padding-left: 9px; line-height: 17px; }
  .search-box svg { position: absolute; right: 7px; top: 4px; }
  .copyright { position: absolute; left: 0; top: 574px; width: 176px; text-align: center; font-size: 10.5px; color: #555; line-height: 14px; }

  .tile-grid { position: absolute; left: 179px; width: 1021px; display: grid; grid-template-columns: repeat(4, 1fr); }
  .tile-grid.top { top: 0; height: 314px; grid-template-rows: 1fr 1fr; }
  .tile-grid.bottom { top: 516px; height: 91px; }
  .photo { width: 100%; height: 100%; }

  .team-tile { background: var(--team-bg); text-align: center; position: relative; }
  .team-heading { width: 196px; height: 46px; margin: 6px auto 0; background: linear-gradient(90deg, #c98fb4, #b86a9c); border-radius: 2px; }
  .team-photo { width: 78px; height: 62px; margin: 11px auto 0; background: linear-gradient(180deg, #5a3d6e, #2a1f36); }
  .team-call { font-size: 21px; line-height: 26px; color: var(--brand); margin-top: 8px; }

  .feature-band { position: absolute; left: 179px; top: 314px; width: 1021px; height: 202px; background: #f7f6f4; }
  .feature-frame { position: absolute; left: 9px; top: 9px; width: 1000px; height: 182px; border: 5px solid var(--frame); background-color: var(--panel); display: flex; }
  .feature { position: relative; flex: 1; }
  .feature + .feature { border-left: 1px solid var(--divider); }
  .feature:nth-child(1) { flex: 0 0 328px; }
  .feature:nth-child(2) { flex: 0 0 335px; }
  .feature-icon { position: absolute; top: 82px; }
  .feature-body { position: absolute; top: 28px; width: 232px; }
  .feature-title { font-family: "Lora", serif; font-weight: 400; font-size: 20px; color: var(--brand); margin-bottom: 8px; }
  .feature-text { font-size: 11.3px; line-height: 14.5px; color: var(--ink); }
  .feature-link { display: inline-block; margin-top: 14px; font-size: 11.3px; color: var(--ink); text-decoration: underline; }
</style>
</head>
<body>

<aside class="sidebar">
  <div class="brand">
    <div class="brand-name">Coral Belle Events</div>
    <div class="brand-tagline">WEDDINGS, QUINCES &amp; CORP EVENTS</div>
  </div>
  <ul class="main-nav">
    <li class="is-active">Home</li>
    <li>Contact Us</li>
    <li class="has-sub">Locations &amp; Venues</li>
    <li class="has-sub">Services</li>
    <li class="has-sub">About Us</li>
    <li class="has-sub">Catering</li>
    <li class="has-sub">Wedding Packages</li>
    <li class="has-sub is-active">Other Events</li>
    <li class="has-sub">Caribbean Weddings</li>
    <li>Invitations</li>
    <li>Specials</li>
    <li>Blog</li>
    <li>Existing Clients</li>
    <li>Testimonials</li>
  </ul>
  <div class="social-row" aria-label="Social links">
    <span></span><span></span><span></span><span></span><span></span><span></span>
  </div>
  <div class="search-box">Search...
    <svg width="10" height="10" viewBox="0 0 10 10"><circle cx="4" cy="4" r="3" fill="none" stroke="#999" stroke-width="1.2"/><line x1="6.2" y1="6.2" x2="9" y2="9" stroke="#999" stroke-width="1.4"/></svg>
  </div>
  <p class="copyright">© Copyright 2013, All Rights<br>Reserved</p>
</aside>

<section class="tile-grid top">
  <div class="photo" role="img" aria-label="Villa with pool at dusk" style="background:linear-gradient(180deg,#8fa3c4 0%,#b77b5e 45%,#4f8aa8 75%,#6b5a44 100%)"></div>
  <div class="photo" role="img" aria-label="Ballroom lit in purple" style="background:radial-gradient(circle at 50% 55%,#e6a8f0 0%,#a433c9 45%,#5e1379 100%)"></div>
  <div class="photo" role="img" aria-label="Champagne toast" style="background:linear-gradient(135deg,#2a2a2a 0%,#6e6e6e 40%,#d9cfc0 60%,#1c1c1c 100%)"></div>
  <div class="photo" role="img" aria-label="Guests dancing at a reception" style="background:linear-gradient(180deg,#3a2418 0%,#8a5a3c 50%,#4a2e20 100%)"></div>
  <div class="photo" role="img" aria-label="Courtyard arch with palms" style="background:linear-gradient(180deg,#c9d8e8 0%,#e3d9c6 50%,#8a8f6e 100%)"></div>
  <div class="team-tile">
    <div class="team-heading" role="img" aria-label="Hand-lettered heading: Meet the Team"></div>
    <div class="team-photo" role="img" aria-label="Team group photo"></div>
    <div class="team-call">Call us at 305.555.0142</div>
  </div>
  <div class="photo" role="img" aria-label="Bar with checkered floor" style="background:linear-gradient(180deg,#5a2a14 0%,#c0703a 35%,#7a1f1a 60%,#777 80%,#222 100%)"></div>
  <div class="photo" role="img" aria-label="Church beside city towers" style="background:linear-gradient(180deg,#7fb3e6 0%,#b8cde0 40%,#d8c9b0 70%,#7a8a6a 100%)"></div>
</section>

<section class="feature-band">
  <div class="feature-frame">
    <div class="feature">
      <svg class="feature-icon" style="left:24px" width="40" height="42" viewBox="0 0 40 42" aria-hidden="true">
        <g fill="none" stroke="var(--brand)" stroke-width="3">
          <circle cx="15" cy="24" r="10"/><circle cx="25" cy="28" r="10"/>
          <path d="M11 12 l4 -6 l4 6"/>
        </g>
      </svg>
      <div class="feature-body" style="left:82px">
        <h2 class="feature-title">Weddings</h2>
        <p class="feature-text">Lorem ipsum dolor sit amet, consectetur adipiscing elit. Nunc eget arcu vitae risus blandit vulputate. Cum sociis natoque penatibus et magnis dis parturient montes, nascetur ridiculus mus.</p>
        <a class="feature-link">click here for more details</a>
      </div>
    </div>
    <div class="feature">
      <svg class="feature-icon" style="left:28px" width="36" height="42" viewBox="0 0 36 42" aria-hidden="true">
        <g fill="none" stroke="var(--brand)" stroke-width="2.5" stroke-linejoin="round">
          <path d="M3 8 H31 L17 24 Z" fill="var(--brand)"/>
          <line x1="17" y1="24" x2="17" y2="38"/><line x1="9" y1="39" x2="25" y2="39"/>
          <line x1="20" y1="12" x2="30" y2="1"/><circle cx="29" cy="9" r="3.5"/>
        </g>
      </svg>
      <div class="feature-body" style="left:81px">
        <h2 class="feature-title">Parties</h2>
        <p class="feature-text">Lorem ipsum dolor sit amet, consectetur adipiscing elit. Nunc eget arcu vitae risus blandit vulputate. Cum sociis natoque penatibus et magnis dis parturient montes, nascetur ridiculus mus.</p>
        <a class="feature-link">click here for more details</a>
      </div>
    </div>
    <div class="feature">
      <svg class="feature-icon" style="left:27px" width="36" height="42" viewBox="0 0 36 42" aria-hidden="true">
        <g fill="none" stroke="var(--brand)" stroke-width="3" stroke-linejoin="round">
          <path d="M4 10 q3 -7 10 -5 q6 -4 12 2 q4 1 2 6" />
          <rect x="4" y="12" width="22" height="27" rx="2"/>
          <path d="M26 17 h5 a3 3 0 0 1 3 3 v9 a3 3 0 0 1 -3 3 h-5"/>
          <line x1="11" y1="18" x2="11" y2="34"/><line x1="19" y1="18" x2="19" y2="34"/>
        </g>
      </svg>
      <div class="feature-body" style="left:80px">
        <h2 class="feature-title">Corporate events</h2>
        <p class="feature-text">Lorem ipsum dolor sit amet, consectetur adipiscing elit. Nunc eget arcu vitae risus blandit vulputate. Cum sociis natoque penatibus et magnis dis parturient montes, nascetur ridiculus mus.</p>
        <a class="feature-link">click here for more details</a>
      </div>
    </div>
  </div>
</section>

<section class="tile-grid bottom">
  <div class="photo" role="img" aria-label="Venue terrace at twilight" style="background:linear-gradient(180deg,#5d7fa8 0%,#3b3f3a 60%,#c9a46a 100%)"></div>
  <div class="photo" role="img" aria-label="Evening patio with purple lights" style="background:linear-gradient(90deg,#3a2a20 0%,#6b4a3a 50%,#8a2fb0 100%)"></div>
  <div class="photo" role="img" aria-label="Hotel facade under blue sky" style="background:linear-gradient(180deg,#3f7fd0 0%,#9fc0e0 45%,#c99a7a 70%,#4f7a3a 100%)"></div>
  <div class="photo" role="img" aria-label="Waterfront mansion with palms" style="background:linear-gradient(180deg,#8fb8e0 0%,#d8e4ee 50%,#5f7a4a 100%)"></div>
</section>

</body>
</html>
```